Restaurant service company needs a website!

I am looking for a skilled web designer/developer to create a professional, responsive, and easy-to-navigate website for my company, which specializes in servicing restaurant cooking equipment. The site should communicate trust, reliability, and technical expertise to our target audience, restaurant owners, managers, and commercial kitchen operators. I have included the company logos, if any other format for them is needed please let me know.

Target Market(s)

restaurant owners, managers, and commercial kitchen operators

Industry/Entity Type

Commercial Kitchen Equipment Service

Coding

Coded - Design and coding required

Number of Pages Required

1 page

Font styles to use
Serif
Sans Serif

Requirements
Must have
• Contact and service request forms, Click-to-call functionality for mobile, Clean, modern layout with strong visuals, Easy navigation, mobile-friendly
Nice to have
• Testimonials or Reviews, If possible a click-to-text functionality for mobile.
Should not have
• Any mention of Refrigeration or HVAC, "Free Quotes"

```html
<!DOCTYPE html>
<html lang="en">
<head>
<meta charset="utf-8">
<title>Keystone Restaurant Service</title>
<link href="https://fonts.googleapis.com/css2?family=PT+Serif:wght@400;700&family=Poppins:wght@400;500;600&display=swap" rel="stylesheet">
<style>
:root{
  --teal:#1d6177;
  --teal-dark:#1a5567;
  --teal-label:#2b7a92;
  --gold:#e8b400;
  --ink:#111417;
  --body:#3a3f44;
  --mist:#dce9ed;
  --white:#ffffff;
  --serif:"PT Serif",Georgia,serif;
  --sans:"Poppins",Arial,sans-serif;
}
*{box-sizing:border-box;margin:0;padding:0}
html,body{width:1200px;height:4112px;overflow:hidden;background:var(--white);font-family:var(--sans);color:var(--ink)}
.page{position:relative;width:1200px;height:4112px}
.abs{position:absolute}
.label{font-family:var(--sans);font-size:19px;color:var(--teal-label);letter-spacing:.3px}
.heading{font-family:var(--serif);font-weight:700;font-size:44px;line-height:1.12;color:var(--ink)}
.btn{position:absolute;background:var(--gold);color:#1b1b1b;font-weight:600;font-size:14px;border-radius:5px;display:flex;align-items:center;justify-content:center;letter-spacing:.2px}
.photo{position:absolute}

/* nav */
.brand{left:78px;top:16px;height:44px;display:flex;align-items:center;gap:10px}
.brand-mark{width:30px;height:30px;border:2px solid var(--teal)}
.brand-name{font-family:var(--sans);font-weight:600;font-size:21px;color:var(--teal);line-height:1}
.nav{left:535px;top:28px;display:flex;gap:27px;font-size:15px;color:var(--ink)}
.nav-cta{left:990px;top:16px;width:134px;height:40px;background:var(--teal);color:#fff;border-radius:5px;font-size:14px;font-weight:600;display:flex;align-items:center;justify-content:center}

/* hero */
.hero{left:26px;top:75px;width:1148px;height:543px;border-radius:16px;background:linear-gradient(160deg,#d8dadb 0%,#a9adb0 45%,#6d7175 100%);overflow:hidden}
.hero::after{content:"";position:absolute;inset:0;background:linear-gradient(90deg,rgba(20,25,30,.55),rgba(20,25,30,.05) 60%)}
.hero-title{left:75px;top:386px;font-family:var(--serif);font-weight:700;font-size:64px;color:#fff;line-height:1.05;z-index:1}
.hero-sub{left:75px;top:458px;font-family:var(--serif);font-size:45px;color:#fff;z-index:1}

/* about */
.about-photo{left:74px;top:702px;width:480px;height:523px;background:linear-gradient(150deg,#3a3f45,#8a8e93 40%,#c0692c 70%,#2a2d31)}
.about-text{left:609px;top:720px;width:510px}
.about-text .heading{margin-top:8px}
.about-text p{margin-top:16px;font-size:13.4px;line-height:1.62;color:var(--body)}
.about-panel{left:553px;top:1025px;width:571px;height:200px;background:var(--mist);border-top-right-radius:64px}
.pillar{position:absolute;top:30px;width:210px}
.pillar-icon{width:48px;height:48px;border-radius:50%;background:#fff;display:flex;align-items:center;justify-content:center}
.pillar h3{font-weight:500;font-size:20px;margin-top:14px}
.pillar p{font-size:12.5px;line-height:1.55;color:var(--body);margin-top:6px}
.pillar-divider{position:absolute;left:283px;top:30px;width:1px;height:146px;background:var(--teal-label)}

/* services */
.center{left:0;width:1200px;text-align:center}
.card{position:absolute;top:1467px;width:248px;height:219px;background:#fff;border-radius:8px;box-shadow:0 2px 12px rgba(0,0,0,.12);text-align:center;padding-top:18px}
.card-icon{width:54px;height:54px;border-radius:50%;background:var(--teal);margin:0 auto;display:flex;align-items:center;justify-content:center;box-shadow:0 0 0 4px #d2e4ea}
.card h3{font-weight:500;font-size:21px;line-height:1.27;margin-top:14px}
.card p{font-size:11.6px;line-height:1.65;color:var(--body);margin-top:8px;padding:0 22px}

/* gallery */
.gallery-band{left:0;top:1842px;width:1200px;height:235px;background:var(--teal-dark)}
.gallery-title{top:1910px;font-family:var(--serif);font-weight:700;font-size:44px;color:#fff}
.gallery-copy{left:265px;top:1975px;width:670px;text-align:center;font-size:13.4px;line-height:1.62;color:#fff}
.shot{top:2077px;height:301px;border-radius:6px}
.dots{left:509px;top:2406px;display:flex;gap:6px}
.dots span{height:3px;width:24px;background:#d0d4d7}
.dots span.on{width:60px;background:var(--teal)}

/* testimonials */
.testi-band{left:0;top:2493px;width:1200px;height:510px;background:var(--mist)}
.t-card{position:absolute;top:2682px;width:367px;height:240px;background:#fff;border-radius:6px;box-shadow:0 2px 10px rgba(0,0,0,.08);padding:36px 14px 0 110px}
.t-photo{position:absolute;top:2703px;width:232px;height:195px}
.t-quote{position:absolute;left:53px;top:18px;width:38px;height:38px;border-radius:50%;background:#fff;box-shadow:0 1px 6px rgba(0,0,0,.15);display:flex;align-items:center;justify-content:center}
.t-card h4{font-weight:600;font-size:18px}
.stars{color:var(--gold);font-size:11px;letter-spacing:2px;margin-top:2px}
.t-card p{font-size:11.8px;line-height:1.72;color:var(--body);margin-top:8px}
.arrow{position:absolute;top:2781px;width:38px;height:38px;border-radius:50%;border:2px solid var(--teal-label);display:flex;align-items:center;justify-content:center}

/* contact */
.contact-head{left:80px;top:3100px}
.contact-copy{left:80px;top:3162px;width:470px;font-size:13.4px;line-height:1.62;color:var(--body)}
.field{position:absolute;height:40px;border:1px solid #9fb7bf;border-radius:5px;background:#f4f8f9;font-size:13px;color:#333;padding:11px 14px}
.contact-photo{left:639px;top:3085px;width:485px;height:525px;border-radius:14px;background:linear-gradient(160deg,#c9ccce,#8f8b86 50%,#5b5f63)}

/* footer */
.footer{left:0;top:3692px;width:1200px;height:420px;background:var(--teal-dark);color:#fff}
.f-brand{position:absolute;left:88px;top:80px;width:170px;text-align:center}
.f-mark{width:90px;height:90px;border:3px solid #fff;margin:0 auto}
.f-name{font-weight:600;font-size:24px;margin-top:20px;line-height:1}
.f-tag{font-size:10.5px;letter-spacing:3px;margin-top:6px}
.f-col{position:absolute;top:88px}
.f-col h5{font-family:var(--sans);font-weight:600;font-size:26px;margin-bottom:8px}
.f-col li{list-style:none;font-size:14.5px;line-height:28.5px}
.f-contact li{display:flex;align-items:center;gap:8px;line-height:34px;font-size:14px}
.f-rule{position:absolute;left:0;top:338px;width:1200px;height:1px;background:rgba(255,255,255,.35)}
.f-copy{position:absolute;left:80px;top:370px;font-size:15px}
.socials{position:absolute;left:985px;top:362px;display:flex;gap:14px}
.socials span{width:34px;height:34px;border:1.5px solid #fff;border-radius:50%;display:flex;align-items:center;justify-content:center}
.socials i{display:block;width:12px;height:12px;background:#fff;border-radius:3px}
</style>
</head>
<body>
<div class="page">

  <!-- Header -->
  <div class="abs brand"><span class="brand-mark"></span><span class="brand-name">KEYSTONE</span></div>
  <nav class="abs nav"><span>Home</span><span>About Us</span><span>Services</span><span>Gallery</span><span>Testimonials</span></nav>
  <a class="abs nav-cta">CONTACT US</a>

  <!-- Hero -->
  <div class="photo hero" role="img" aria-label="Stainless steel commercial kitchen with pots, shelves and ovens"></div>
  <h1 class="abs hero-title">Expert Care for Your</h1>
  <div class="abs hero-sub">Commercial Kitchen Equipment</div>
  <a class="btn" style="left:75px;top:528px;width:179px;height:40px">REQUEST SERVICE</a>

  <!-- About -->
  <div class="photo about-photo" role="img" aria-label="Chef cooking with flames over a commercial range"></div>
  <div class="abs about-text">
    <div class="label">ABOUT US</div>
    <h2 class="heading">Keeping Your Kitchen<br>Running, 24/7</h2>
    <p>Lorem Ipsum is simply dummy text of the printing and typesetting industry. Lorem Ipsum has been the industry's standard dummy text ever since the 1500s, when an unknown printer took a galley of type and scrambled it to make a type specimen book. It has survived not only five centuries, but also the leap into electronic typesetting, remaining essentially.</p>
  </div>
  <div class="abs about-panel">
    <div class="pillar" style="left:56px">
      <div class="pillar-icon"><svg width="30" height="22" viewBox="0 0 30 22" fill="none" stroke="#1d6177" stroke-width="2"><circle cx="8" cy="14" r="6"/><circle cx="22" cy="14" r="6"/><path d="M14 12h2M5 8l3-6h3M25 8l-3-6h-3"/></svg></div>
      <h3>Our Vision</h3>
      <p>Lorem Ipsum is simply dummy text of the printing and typesetting industry.</p>
    </div>
    <div class="pillar-divider"></div>
    <div class="pillar" style="left:336px">
      <div class="pillar-icon"><svg width="28" height="28" viewBox="0 0 28 28" fill="none" stroke="#1d6177" stroke-width="2"><circle cx="14" cy="14" r="11"/><circle cx="14" cy="14" r="6.5"/><circle cx="14" cy="14" r="2"/><path d="M14 14l10-10"/></svg></div>
      <h3>Our Mission</h3>
      <p>Lorem Ipsum is simply dummy text of the printing and typesetting industry.</p>
    </div>
  </div>

  <!-- Services -->
  <div class="abs center label" style="top:1303px">OUR SERVICES</div>
  <h2 class="abs center heading" style="top:1334px">Exceptional Craftsmanship,<br>Endless Possibilities</h2>

  <div class="card" style="left:74px">
    <div class="card-icon"><svg width="28" height="28" viewBox="0 0 28 28" fill="none" stroke="#fff" stroke-width="1.8"><rect x="4" y="6" width="20" height="17" rx="2"/><path d="M4 11h20"/><circle cx="10" cy="17" r="3"/><circle cx="19" cy="17" r="3"/></svg></div>
    <h3>Cooking<br>Equipment Repair</h3>
    <p>Lorem Ipsum Is Simply Dummy Text Of The Printing And Industry. Lorem Ipsum Has Been..</p>
  </div>
  <div class="card" style="left:342px">
    <div class="card-icon"><svg width="28" height="28" viewBox="0 0 28 28" fill="none" stroke="#fff" stroke-width="1.8"><rect x="5" y="5" width="18" height="18" rx="2"/><circle cx="14" cy="14" r="4"/><path d="M9 9h3M16 20l4 4"/></svg></div>
    <h3>Preventive<br>Maintenance</h3>
    <p>Lorem Ipsum Is Simply Dummy Text Of The Printing And Industry. Lorem Ipsum Has Been..</p>
  </div>
  <div class="card" style="left:609px">
    <div class="card-icon"><svg width="28" height="28" viewBox="0 0 28 28" fill="none" stroke="#fff" stroke-width="1.8"><circle cx="14" cy="14" r="5"/><path d="M14 3v4M14 21v4M3 14h4M21 14h4M6 6l3 3M19 19l3 3M22 6l-3 3M9 19l-3 3"/></svg></div>
    <h3>Installation<br>&amp; Setup</h3>
    <p>Lorem Ipsum Is Simply Dummy Text Of The Printing And Industry. Lorem Ipsum Has Been..</p>
  </div>
  <div class="card" style="left:876px">
    <div class="card-icon"><svg width="28" height="28" viewBox="0 0 28 28" fill="none" stroke="#fff" stroke-width="1.8"><path d="M6 22L20 8M18 4l6 6-3 1-4-4zM6 6l16 16M4 8l4-4"/></svg></div>
    <h3>Emergency<br>Repairs</h3>
    <p>Lorem Ipsum Is Simply Dummy Text Of The Printing And Industry. Lorem Ipsum Has Been..</p>
  </div>
  <a class="btn" style="left:510px;top:1718px;width:180px;height:40px">REQUEST SERVICE</a>

  <!-- Gallery -->
  <div class="abs gallery-band"></div>
  <h2 class="abs center gallery-title">Our Gallery</h2>
  <p class="abs gallery-copy">Lorem Ipsum is simply dummy text of the printing and typesetting industry. Lorem Ipsum has been the industry's standard dummy text ever since the 1500s, when an unknown printer took a galley of type and scrambled it to make a type specimen book.</p>
  <div class="photo shot" style="left:-10px;width:73px;background:linear-gradient(160deg,#c7cacc,#8d9195)" role="img" aria-label="Kitchen interior, partially visible"></div>
  <div class="photo shot" style="left:79px;width:337px;background:linear-gradient(160deg,#d8d3cc,#9a9590 55%,#6c625a)" role="img" aria-label="Stainless steel commercial ovens under a hood"></div>
  <div class="photo shot" style="left:431px;width:337px;background:linear-gradient(160deg,#e6e7e8,#a8acaf 55%,#3b3f44)" role="img" aria-label="Cook working at a steel kitchen station"></div>
  <div class="photo shot" style="left:783px;width:338px;background:linear-gradient(160deg,#e2e4e5,#b4b8bb 55%,#7e8387)" role="img" aria-label="Clean commercial kitchen with range and prep tables"></div>
  <div class="photo shot" style="left:1136px;width:74px;background:linear-gradient(160deg,#b9bdc0,#5f6469)" role="img" aria-label="Kitchen interior, partially visible"></div>
  <div class="abs dots"><span class="on"></span><span></span><span></span><span></span><span></span></div>

  <!-- Testimonials -->
  <div class="abs testi-band"></div>
  <div class="abs center label" style="top:2570px">TESTIMONIALS</div>
  <h2 class="abs center heading" style="top:2600px">What Our customer says</h2>

  <div class="arrow" style="left:19px"><svg width="18" height="14" viewBox="0 0 18 14" fill="none" stroke="#2b7a92" stroke-width="2"><path d="M17 7H2M7 1L1 7l6 6"/></svg></div>
  <div class="arrow" style="left:1143px"><svg width="18" height="14" viewBox="0 0 18 14" fill="none" stroke="#2b7a92" stroke-width="2"><path d="M1 7h15M11 1l6 6-6 6"/></svg></div>

  <div class="t-card" style="left:224px">
    <div class="t-quote"><svg width="20" height="16" viewBox="0 0 20 16" fill="#1d6177"><path d="M0 16V9C0 4 3 1 8 0v3C5 4 4 6 4 8h4v8zM11 16V9c0-5 3-8 8-9v3c-3 1-4 3-4 5h4v8z"/></svg></div>
    <h4>Daniel Reyes</h4>
    <div class="stars">★★★★★</div>
    <p>Aenean Mauris Magna, Venenatis Vitae Purus Ac, Bibendum Vulputate Magna. Nunc Ante Quam, Consequat At Pulvinar Nec, Feugiat Ac Urna. Class Aptent Taciti Sociosqu Ad Litora Torquent Per Conubia Nostra, Per Inceptos Himenaeos.</p>
  </div>
  <div class="photo t-photo" style="left:74px;background:linear-gradient(160deg,#5a4638,#8a6d58 55%,#2f2a27)" role="img" aria-label="Portrait of a smiling customer in a blazer"></div>

  <div class="t-card" style="left:760px">
    <div class="t-quote"><svg width="20" height="16" viewBox="0 0 20 16" fill="#1d6177"><path d="M0 16V9C0 4 3 1 8 0v3C5 4 4 6 4 8h4v8zM11 16V9c0-5 3-8 8-9v3c-3 1-4 3-4 5h4v8z"/></svg></div>
    <h4>Maya Collins</h4>
    <div class="stars">★★★★★</div>
    <p>Aenean Mauris Magna, Venenatis Vitae Purus Ac, Bibendum Vulputate Magna. Nunc Ante Quam, Consequat At Pulvinar Nec, Feugiat Ac Urna. Class Aptent Taciti Sociosqu Ad Litora Torquent Per Conubia Nostra, Per Inceptos Himenaeos.</p>
  </div>
  <div class="photo t-photo" style="left:610px;background:linear-gradient(160deg,#6e5a4e,#b59c88 50%,#7d8e8a)" role="img" aria-label="Portrait of a smiling restaurant owner holding a tablet"></div>

  <!-- Contact -->
  <h2 class="abs heading contact-head">Contact Us</h2>
  <p class="abs contact-copy">Lorem Ipsum is simply dummy text of the printing and typesetting industry. Lorem Ipsum has been the industry's standard dummy.</p>
  <div class="field" style="left:76px;top:3228px;width:232px">First Name:</div>
  <div class="field" style="left:323px;top:3228px;width:232px">Last Name:</div>
  <div class="field" style="left:76px;top:3284px;width:232px">Email Id:</div>
  <div class="field" style="left:323px;top:3284px;width:232px">Phone No:</div>
  <div class="field" style="left:76px;top:3340px;width:479px;height:108px">Massage Here:</div>
  <a class="btn" style="left:74px;top:3462px;width:481px;height:40px">SUBMIT NOW</a>
  <div class="photo contact-photo" role="img" aria-label="Technician repairing a kitchen extractor hood"></div>

  <!-- Footer -->
  <footer class="abs footer">
    <div class="f-brand">
      <div class="f-mark"></div>
      <div class="f-name">KEYSTONE</div>
      <div class="f-tag">RESTAURANT SERVICE</div>
    </div>
    <div class="f-col" style="left:346px">
      <h5>Quick Link</h5>
      <ul><li>Home</li><li>About Us</li><li>Services</li><li>Gallery</li><li>Testimonials</li><li>Contact US</li></ul>
    </div>
    <div class="f-col" style="left:562px">
      <h5>Our Services</h5>
      <ul><li>Cooking Equipment Repair</li><li>Preventive Maintenance</li><li>Installation &amp; Setup</li><li>Emergency Repairs</li></ul>
    </div>
    <div class="f-col f-contact" style="left:847px">
      <h5>Contact Us</h5>
      <ul>
        <li><svg width="13" height="13" viewBox="0 0 24 24" fill="#fff"><path d="M6.6 10.8a15 15 0 006.6 6.6l2.2-2.2c.3-.3.7-.4 1-.2 1.1.4 2.3.6 3.6.6.6 0 1 .4 1 1V20c0 .6-.4 1-1 1A17 17 0 013 4c0-.6.4-1 1-1h3.5c.6 0 1 .4 1 1 0 1.3.2 2.5.6 3.6.1.3 0 .7-.2 1z"/></svg>555-0142-736</li>
        <li><svg width="14" height="11" viewBox="0 0 24 18" fill="#fff"><path d="M0 0h24v18H0zM2 2l10 8 10-8" stroke="#1a5567" stroke-width="2"/></svg>info@keystonerestaurantservice</li>
        <li><svg width="11" height="15" viewBox="0 0 16 22" fill="#fff"><path d="M8 0a8 8 0 00-8 8c0 6 8 14 8 14s8-8 8-14a8 8 0 00-8-8zm0 11a3 3 0 110-6 3 3 0 010 6z"/></svg>418 Harbor Lane, Suite 12</li>
      </ul>
    </div>
    <div class="f-rule"></div>
    <div class="f-copy">© 2025 Keystone Restaurant Services All Rights Reserved.</div>
    <div class="socials"><span><i></i></span><span><i></i></span><span><i></i></span></div>
  </footer>

</div>
</body>
</html>
```